Flyer Design for Private Car Service

Flyer should cater to Business Travelers and Executives who travel Business Class or First Class.
Flyer should include images attached.
Flyer should include the below text
Dallas to Austin
Chauffeured SUVs
• Travel Dallas to Austin in a new 2025 Marlow Strider for $499 one-way
• Trip includes a Uniformed Chauffeur who has a Commercial Drivers License (CDL)
• You can Schedule Chauffeur Pickup at Your Home in Dallas
• Our Chauffeur will Drop You Off at Your Final Destination in Austin
• You can Schedule Chauffeur Return Pickup in Austin and Return Back to Dallas.
• We offer Faster Times on Door-to-Door Travel than Bluecrest Airways
• We offer Comparable Prices on Door-to-Door Travel Times than Bluecrest Airways
• All of our trips are insured with $500k of commercial auto insurance
• Our Passengers can Talk on Cell Phone & Conduct Quill calls Throughout Travel
• Our Passengers have Maximum Privacy, Comfort and First-Class Amenities.
• Our Passengers Avoid Harwick Vale Field and KPR Airport hassles & delays
• Member Brenton Chamber of Commerce, Larkmoor Chamber of Commerce.
• Book your trip today at www.ridemarquel.example
Target Market(s)
Business Travelers
Look and feel
Each slider illustrates characteristics of the customer's brand and the style your logo design should communicate.

```html
<!DOCTYPE html>
<html lang="en">
<head>
<meta charset="utf-8">
<title>Dallas to Austin Chauffeured SUVs</title>
<link href="https://fonts.googleapis.com/css2?family=Barlow+Condensed:ital,wght@1,800&family=Poppins:wght@400;700&display=swap" rel="stylesheet">
<style>
  :root {
    --stage: #6b777d;
    --paper: #ffffff;
    --red: #e8243c;
    --ink: #111111;
    --text: #1c1c1c;
    --photo-main: linear-gradient(180deg, #d9d4cc 0%, #3a3d42 45%, #b9b6b1 75%, #cfccc7 100%);
    --photo-left: linear-gradient(135deg, #8c9096 0%, #1d1f24 50%, #5b4a3f 100%);
    --photo-right: linear-gradient(135deg, #c9d2d8 0%, #2a2c30 55%, #9a8e86 100%);
  }
  * { box-sizing: border-box; margin: 0; padding: 0; }
  html, body { width: 1200px; height: 1200px; overflow: hidden; background: var(--stage); }
  .flyer {
    position: absolute; left: 193px; top: 30px; width: 814px; height: 1140px;
    background: var(--paper); overflow: hidden;
    font-family: "Poppins", sans-serif; color: var(--text);
  }
  .header-shapes { position: absolute; left: 0; top: 0; width: 814px; height: 175px; }
  .brand {
    position: absolute; left: 0; top: 0; width: 330px; height: 167px;
    display: flex; align-items: center; justify-content: center; gap: 10px;
  }
  .brand-dot { width: 14px; height: 14px; border-radius: 50%; background: var(--red); }
  .brand-name { font-family: "Poppins", sans-serif; font-weight: 400; font-size: 30px; letter-spacing: 4px; color: var(--ink); text-transform: uppercase; }
  .headline {
    position: absolute; right: 47px; top: 36px; text-align: right;
    font-family: "Barlow Condensed", sans-serif; font-style: italic; font-weight: 800;
    font-size: 52px; line-height: 51px; color: #fff; text-transform: uppercase; letter-spacing: 1px;
  }
  .photo { position: absolute; }
  .photo-main { left: 0; top: 175px; width: 814px; height: 223px; background: var(--photo-main); }
  .photo-boarding { left: 0; top: 406px; width: 402px; height: 146px; background: var(--photo-left); }
  .photo-team { left: 411px; top: 406px; width: 403px; height: 146px; background: var(--photo-right); }
  .divider { position: absolute; left: 0; top: 560px; width: 814px; height: 8px; }
  .benefit {
    position: absolute; display: flex; gap: 8px;
    font-size: 17px; line-height: 21px; color: var(--text);
  }
  .benefit svg { flex: none; width: 17px; height: 17px; margin-top: 1px; }
  .col-left { left: 49px; width: 340px; }
  .col-right { left: 423px; width: 360px; }
  .footer { position: absolute; left: 0; top: 1053px; width: 814px; height: 87px; }
  .footer-cta {
    position: absolute; left: 90px; top: 1053px; height: 87px; line-height: 87px;
    font-weight: 700; font-size: 24px; color: #fff; white-space: nowrap;
  }
  .footer-url {
    position: absolute; left: 445px; top: 1053px; height: 87px; line-height: 87px;
    font-weight: 400; font-size: 26px; color: #fff; white-space: nowrap;
  }
</style>
</head>
<body>
<main class="flyer">
  <svg class="header-shapes" viewBox="0 0 814 175" aria-hidden="true">
    <rect x="0" y="167" width="814" height="8" fill="var(--red)"/>
    <polygon points="352,0 814,0 814,175 301,175" fill="var(--red)"/>
    <polygon points="341,0 352,0 301,167 290,167" fill="var(--ink)"/>
  </svg>
  <div class="brand">
    <span class="brand-dot"></span>
    <span class="brand-name">Marquel</span>
  </div>
  <h1 class="headline">Dallas to Austin<br>Chauffeured SUVs</h1>

  <div class="photo photo-main" role="img" aria-label="Uniformed chauffeurs standing beside three SUVs in front of a glass building"></div>
  <div class="photo photo-boarding" role="img" aria-label="Chauffeur opening the door of a black SUV for a business traveler"></div>
  <div class="photo photo-team" role="img" aria-label="Row of uniformed chauffeurs in caps and black jackets"></div>

  <svg class="divider" viewBox="0 0 814 8" aria-hidden="true">
    <polygon points="0,0 402,0 398,8 0,8" fill="var(--ink)"/>
    <polygon points="410,0 814,0 814,8 406,8" fill="var(--red)"/>
  </svg>

  <svg width="0" height="0" style="position:absolute">
    <symbol id="tick" viewBox="0 0 20 20">
      <circle cx="10" cy="10" r="10" fill="var(--red)"/>
      <path d="M5.5 10.3 L8.6 13.3 L14.6 7" fill="none" stroke="#fff" stroke-width="2.4" stroke-linecap="round" stroke-linejoin="round"/>
    </symbol>
  </svg>

  <ul class="benefits" style="list-style:none">
    <li class="benefit col-left" style="top:600px"><svg><use href="#tick"/></svg><span>Travel Dallas to Austin in a new 2025 Marlow Strider for $499 one way</span></li>
    <li class="benefit col-left" style="top:669px"><svg><use href="#tick"/></svg><span>Trip includes a Uniformed Chauffeur who has a Commercial Drivers License (CDL)</span></li>
    <li class="benefit col-left" style="top:756px"><svg><use href="#tick"/></svg><span>You can Schedule Chauffeur Pickup at Your Home in Dallas</span></li>
    <li class="benefit col-left" style="top:816px"><svg><use href="#tick"/></svg><span>Our Chauffeur will Drop You Off at Your Final Destination in Austin</span></li>
    <li class="benefit col-left" style="top:880px"><svg><use href="#tick"/></svg><span>You can Schedule Chauffeur Return Pickup in Austin and Return Back to Dallas.</span></li>
    <li class="benefit col-left" style="top:967px"><svg><use href="#tick"/></svg><span>We offer Faster Times on Door-to-Door Travel than Bluecrest Airways</span></li>

    <li class="benefit col-right" style="top:599px"><svg><use href="#tick"/></svg><span>We offer Comparable Prices<br>on Door-to-Door Travel Times<br>than Bluecrest Airways</span></li>
    <li class="benefit col-right" style="top:682px"><svg><use href="#tick"/></svg><span>All of our trips are insured with $500k of commercial auto insurance</span></li>
    <li class="benefit col-right" style="top:744px"><svg><use href="#tick"/></svg><span>Our Passengers can Talk on Cell Phone &amp; Conduct Quill calls Throughout Travel</span></li>
    <li class="benefit col-right" style="top:827px"><svg><use href="#tick"/></svg><span>Our Passengers have Maximum Privacy, Comfort and First-Class Amenities.</span></li>
    <li class="benefit col-right" style="top:910px"><svg><use href="#tick"/></svg><span>Our Passengers Avoid Harwick Vale Field and KPR Airport hassles &amp; delays</span></li>
    <li class="benefit col-right" style="top:971px"><svg><use href="#tick"/></svg><span>Member Brenton Chamber of Commerce, Larkmoor Chamber of Commerce.</span></li>
  </ul>

  <svg class="footer" viewBox="0 0 814 87" aria-hidden="true">
    <rect x="0" y="0" width="814" height="87" fill="var(--red)"/>
    <polygon points="0,0 423,0 397,87 0,87" fill="var(--ink)"/>
    <polygon points="423,0 428,0 402,87 397,87" fill="#fff"/>
  </svg>
  <p class="footer-cta">Book your trip today at</p>
  <p class="footer-url">www.ridemarquel.example</p>
</main>
</body>
</html>
```